wisdom by sparks community

The website presents a new interactive learning system where it provides not only the teaching material as the instructor friend who can both teach and learn, making friends and making money.
Make friends and get money.

Learn

```html
<!DOCTYPE html>
<html lang="en">
<head>
<meta charset="utf-8">
<title>Wisdom by Sparks — Learn from the Professionals</title>
<link rel="stylesheet" href="https://fonts.googleapis.com/css2?family=Bebas+Neue&family=Lato:ital,wght@1,400&display=swap">
<style>
  :root {
    --white: #ffffff;
    --field-border: rgba(255, 255, 255, 0.85);
    --nav-cyan: #14d3e2;
    --shade-dark: #3b2f27;
    --shade-warm: #8a6a4f;
    --shade-light: #c9b7a2;
    --shade-shelf: #6b4a35;
  }
  * { box-sizing: border-box; margin: 0; padding: 0; }
  html, body {
    width: 1200px;
    height: 657px;
    overflow: hidden;
    background: var(--shade-dark);
  }
  .page {
    position: relative;
    width: 1200px;
    height: 657px;
    font-family: "Bebas Neue", "Oswald", sans-serif;
    color: var(--white);
  }
  .hero-photo {
    position: absolute;
    inset: 0 0 46px 0;
    background:
      linear-gradient(180deg, rgba(0,0,0,0.15), rgba(0,0,0,0.25)),
      radial-gradient(ellipse 260px 330px at 640px 330px, #b9a493 0%, rgba(185,164,147,0) 100%),
      linear-gradient(90deg,
        #7d6a5c 0%,
        var(--shade-warm) 18%,
        #a08468 32%,
        var(--shade-light) 50%,
        #a48c7a 66%,
        var(--shade-shelf) 78%,
        #7a5a48 90%,
        #9a7a66 100%);
  }
  .brand {
    position: absolute;
    top: 26px;
    left: 0;
    width: 1200px;
    text-align: center;
  }
  .brand-dot {
    display: block;
    width: 14px;
    height: 14px;
    margin: 0 auto 14px;
    border-radius: 50%;
    background: var(--white);
  }
  .brand-name {
    font-size: 38px;
    line-height: 1;
    letter-spacing: 0.5px;
  }
  .headline {
    position: absolute;
    top: 232px;
    left: 0;
    width: 1200px;
    text-align: center;
    font-size: 77px;
    line-height: 1;
    font-weight: 400;
  }
  .subline {
    position: absolute;
    top: 322px;
    left: 0;
    width: 1200px;
    text-align: center;
    font-size: 35px;
    line-height: 1;
    font-weight: 400;
  }
  .signup-field {
    position: absolute;
    top: 393px;
    width: 277px;
    height: 39px;
    border: 1px solid var(--field-border);
    background: transparent;
    font-family: "Lato", "Helvetica Neue", sans-serif;
    font-style: italic;
    font-size: 13px;
    color: var(--white);
    padding: 6px 6px 0;
    line-height: 1;
  }
  .signup-field--name { left: 313px; }
  .signup-field--email { left: 607px; }
  .signup-button {
    position: absolute;
    top: 472px;
    left: 536px;
    width: 128px;
    height: 38px;
    border: 1px solid var(--field-border);
    font-size: 22px;
    line-height: 38px;
    text-align: center;
  }
  .main-nav {
    position: absolute;
    left: 0;
    bottom: 0;
    width: 1200px;
    height: 46px;
    background: var(--nav-cyan);
  }
  .nav-link {
    position: absolute;
    top: 8px;
    font-size: 34px;
    line-height: 1;
    transform: translateX(-50%);
  }
</style>
</head>
<body>
  <main class="page">
    <div class="hero-photo" role="img" aria-label="Smiling student with a backpack taking a book from a library shelf, blurred reading room behind"></div>

    <header class="brand">
      <span class="brand-dot"></span>
      <div class="brand-name">WISDOM BY SPARKS</div>
    </header>

    <h1 class="headline">LEARN FROM THE PROFESSIONALS</h1>
    <h2 class="subline">SUBSCRIBE AND GET A FREE ONLINE COURSE</h2>

    <div class="signup-field signup-field--name">Enter Name</div>
    <div class="signup-field signup-field--email">Enter Email</div>
    <div class="signup-button">SUBSCRIBE</div>

    <nav class="main-nav">
      <span class="nav-link" style="left:314px">COURSES</span>
      <span class="nav-link" style="left:479px">TEACHERS</span>
      <span class="nav-link" style="left:682px">PRICING</span>
      <span class="nav-link" style="left:867px">CONTACT</span>
    </nav>
  </main>
</body>
</html>
```